West Calloway Commuter Services Alliance Needs an Ad Showcasing 2012's Accomplishments

The West Calloway Commuter Services Alliance is a nonprofit organization with the mission to foster transportation behaviors that benefit the community through advocacy, programs, education, and services. We have had a great year in 2012 and would like to show the community what we have accomplished.

We would like a FULL PAGE ad that will be used in a color print magazine and a black and white print publication.

The Pelican Loop - Over 75,000 trips taken by shuttle riders, a 120% increase in trips over 2011.

Stride Together Program - During the 2011-2012 school year an average of 897 students walked to school weekly on walk to school days.

Pedal Season Challenge - 41,950 miles were ridden by students and teachers in May 2012 in 9 participating schools.

Wheel Medic - over 600 bikes have been serviced in 2012.

Requirements
Must have
• Contact info:
West Calloway CSA
4827 Ramble Creek Rd
Sacramento, CA 95834
916-555-0173
WCCSA.org

Twitter @West CallowayCSA
Facebook.com/WestCallowayCSA

LOGO

```html
<!DOCTYPE html>
<html lang="en">
<head>
<meta charset="utf-8">
<title>West Calloway CSA – 2012 Accomplishments</title>
<link rel="stylesheet" href="https://fonts.googleapis.com/css2?family=Source+Sans+3:wght@400;600;700&display=swap">
<style>
  :root {
    --page-bg: #e4e4e4;
    --paper: #ffffff;
    --sky-top: #2f8fd8;
    --sky-bottom: #6cc0ee;
    --grass-top: #7cc243;
    --grass-bottom: #4e9a2a;
    --ink: #111111;
    --green: #9dbb1c;
    --purple: #5a58a6;
    --orange: #ec7124;
    --blue: #1b6fb3;
    --logo-ink: #5a58a6;
    --bus: #6d6bc0;
    --white: #ffffff;
  }
  * { box-sizing: border-box; margin: 0; padding: 0; }
  html, body { width: 1200px; height: 907px; overflow: hidden; }
  body {
    background: var(--page-bg);
    font-family: "Source Sans 3", "Myriad Pro", sans-serif;
    position: relative;
  }
  .ad {
    position: absolute;
    left: 300px; top: 27px;
    width: 600px; height: 853px;
    background: var(--paper);
    overflow: hidden;
  }
  .sky {
    position: absolute; left: 0; top: 0; width: 100%; height: 159px;
    background: linear-gradient(180deg, var(--sky-top), var(--sky-bottom));
  }
  .brand {
    position: absolute; left: 208px; top: 61px;
    width: 184px; height: 184px; border-radius: 50%;
    background: var(--paper);
    display: flex; flex-direction: column; align-items: center; justify-content: center;
    gap: 8px; padding: 0 24px; text-align: center;
  }
  .brand-dot {
    width: 56px; height: 56px; border-radius: 50%;
    background: var(--green);
  }
  .brand-name {
    color: var(--logo-ink); font-weight: 700; font-size: 13px; line-height: 1.15;
  }
  .stats {
    position: absolute; left: 0; top: 265px; width: 100%;
    text-align: center;
  }
  .stat { margin-bottom: 23px; }
  .stat-label {
    display: inline-block; width: 261px; height: 38px; line-height: 38px;
    color: var(--white); font-weight: 700; font-size: 22px;
    letter-spacing: -0.2px;
  }
  .label-green { background: var(--green); }
  .label-purple { background: var(--purple); }
  .label-orange { background: var(--orange); }
  .label-blue { background: var(--blue); }
  .stat-text {
    margin-top: 8px;
    color: var(--ink); font-weight: 700; font-size: 17.5px; line-height: 24px;
  }
  .art-bus {
    position: absolute; left: 26px; top: 699px; width: 147px; height: 74px;
  }
  .art-bike {
    position: absolute; left: 476px; top: 710px; width: 99px; height: 63px;
  }
  .grass {
    position: absolute; left: 0; bottom: 0; width: 100%; height: 80px;
    background: linear-gradient(180deg, var(--grass-top), var(--grass-bottom));
    color: var(--white); text-align: center; font-weight: 600;
  }
  .contact { font-size: 13px; margin-top: 18px; }
  .social {
    display: flex; justify-content: center; align-items: center; gap: 40px;
    font-size: 13.5px; margin-top: 11px;
  }
  .social-item { display: flex; align-items: center; gap: 7px; }
  .social-dot {
    width: 17px; height: 17px; border-radius: 50%; background: var(--white);
  }
</style>
</head>
<body>
  <main class="ad">
    <div class="sky"></div>

    <div class="brand">
      <span class="brand-dot"></span>
      <span class="brand-name">West Calloway Commuter Services Alliance</span>
    </div>

    <section class="stats">
      <div class="stat">
        <h2 class="stat-label label-green">The Pelican Loop</h2>
        <p class="stat-text">Over 75,000 trips were taken by shuttle riders in 2012,<br>a 120% increase over 2011.</p>
      </div>
      <div class="stat">
        <h2 class="stat-label label-purple">Stride Together Program</h2>
        <p class="stat-text">During the 2011-2012 school year an average of 897 students<br>walked to school weekly on walk to school days.</p>
      </div>
      <div class="stat">
        <h2 class="stat-label label-orange">Pedal Season Challenge</h2>
        <p class="stat-text">41,950 miles were ridden by students and teachers<br>in May 2012 in 9 participating schools.</p>
      </div>
      <div class="stat">
        <h2 class="stat-label label-blue">Wheel Medic</h2>
        <p class="stat-text">Over 600 bikes have been serviced in 2012.</p>
      </div>
    </section>

    <svg class="art-bus" role="img" aria-label="Illustration of a purple shuttle bus" viewBox="0 0 147 74">
      <rect x="0" y="0" width="147" height="74" rx="14" fill="var(--bus)"/>
    </svg>
    <svg class="art-bike" role="img" aria-label="Illustration of a purple bicycle" viewBox="0 0 99 63">
      <rect x="0" y="0" width="99" height="63" rx="10" fill="var(--bus)" opacity="0.55"/>
    </svg>

    <footer class="grass">
      <p class="contact">West Calloway CSA, 4827 Ramble Creek Rd, Sacramento, CA 95834, 916-555-0173</p>
      <div class="social">
        <span class="social-item"><span class="social-dot"></span>WestCallowayCSA</span>
        <span class="social-item">WCCSA.org</span>
        <span class="social-item"><span class="social-dot"></span>West CallowayCSA</span>
      </div>
    </footer>
  </main>
</body>
</html>
```